Kestrel Dune Line Card

Vibrant Flyer - front and back (line card) with text and collage of pictures. Please include bleed lines. If same picture, use the best of available. Please do not duplicate.

Also include text:
(telephone no.) 888-412-7086
(web address) TallowmereGearHub.com
Rental Sales Service

Target Market(s)

Purchasers of equipment specific to market.

Font styles to use
Sans Serif

Colors
3277b5
fbed22
ec1f27

```html
<!DOCTYPE html>
<html lang="en">
<head>
<meta charset="utf-8">
<title>Kestrel Dune Line Card</title>
<link href="https://fonts.googleapis.com/css2?family=PT+Sans:wght@400;700&family=PT+Sans+Narrow:wght@700&display=swap" rel="stylesheet">
<style>
:root{
  --blue:#3277b5;
  --blue-deep:#1d57a3;
  --yellow:#fbed22;
  --red:#ec1f27;
  --paper:#ffffff;
  --ink:#1a1a1a;
  --stage:#e4e4e2;
}
*{box-sizing:border-box;margin:0;padding:0}
html,body{width:1200px;height:778px;overflow:hidden;background:var(--stage);font-family:"PT Sans",Arial,sans-serif;color:var(--ink)}
.sheet{position:absolute;top:66px;width:498px;height:645px;background:var(--paper);overflow:hidden;box-shadow:0 4px 14px rgba(0,0,0,.25)}
.sheet--front{left:55px}
.sheet--back{left:599px}
.abs{position:absolute}

.brand{position:absolute;top:20px;left:26px;display:flex;align-items:center;gap:8px}
.brand__dot{width:44px;height:44px;border-radius:50%;background:var(--blue)}
.brand__name{font-weight:700;font-size:21px;line-height:1;color:var(--red);width:150px}
.tagline{position:absolute;top:32px;right:20px;text-align:right}
.tagline__services{font-size:16px;font-weight:700;color:var(--ink)}
.tagline__web{font-size:10px;font-weight:700;color:var(--red)}

.photo{position:absolute;border:2px solid #fff;box-shadow:0 1px 3px rgba(0,0,0,.35)}
.photo--warm{background:linear-gradient(135deg,#7a5a3a,#c08a5a 60%,#9b3a30)}
.photo--truck{background:linear-gradient(160deg,#c8a877,#a9998a 40%,#3d3d3d 75%,#8a8a8a)}
.photo--produce{background:linear-gradient(180deg,#c8c8cc,#e06a3a 55%,#c5361c)}
.photo--trailer{background:linear-gradient(160deg,#b83d36,#e3d540 45%,#4a4a40 80%,#6d7a3a)}
.cutout{position:absolute}

.tab{position:absolute;background:var(--blue-deep);color:#fff;font-weight:700;border-radius:0 16px 16px 0;display:flex;align-items:center;padding-left:20px}
.bullets{position:absolute;list-style:none}
.bullets li{position:relative;padding-left:14px}
.bullets li::before{content:"";position:absolute;left:0;top:.35em;width:7px;height:7px;border-radius:50%;background:var(--blue-deep);box-shadow:inset 0 0 0 2px var(--blue-deep)}

.checks{list-style:none}
.checks li{position:relative;padding-left:15px;color:#fff;font-weight:700}
.checks li::before{content:"";position:absolute;left:0;top:.25em;width:9px;height:9px;background:var(--yellow)}
.checks li::after{content:"";position:absolute;left:2px;top:calc(.25em + 1px);width:3px;height:5px;border:solid var(--blue-deep);border-width:0 1.5px 1.5px 0;transform:rotate(45deg)}

.footer{position:absolute;left:0;right:0;bottom:0;height:52px;background:var(--red);display:flex;align-items:center;padding-left:27px}
.footer__cta{color:#fff;font-weight:700;font-size:14px;width:236px}
.footer__phone{display:flex;align-items:center;gap:10px;color:var(--yellow);font-weight:700;font-size:30px}

/* front */
.hero-badge{position:absolute;left:383px;top:197px;width:94px;height:94px;border-radius:50%;background:var(--yellow);border:3px solid #fff;display:flex;align-items:center;justify-content:center;text-align:center;font-family:"PT Sans Narrow","PT Sans",sans-serif;color:var(--blue-deep);font-size:16px;line-height:1.05}
.strengths{position:absolute;left:290px;top:292px;width:198px;height:176px;background:linear-gradient(180deg,var(--blue),var(--blue-deep));border:2px solid #fff;border-radius:0 0 8px 8px;box-shadow:0 1px 3px rgba(0,0,0,.3);padding:14px 8px 0 12px;font-size:8.3px;line-height:14.6px}
.intro{left:27px;top:355px;width:240px;font-size:8.5px;line-height:10.5px}
.intro li+li{margin-top:10px}

/* back */
.benefits-panel{position:absolute;left:239px;top:74px;width:259px;height:519px;background:var(--red)}
.benefits{left:252px;top:126px;width:232px;font-size:7.6px;line-height:9.7px;color:#fff;text-align:justify}
.benefits li{padding-left:12px}
.benefits li::before{background:#fff;box-shadow:none}
.benefits li+li{margin-top:9px}
.equip-box{position:absolute;left:22px;top:338px;width:464px;height:126px;background:linear-gradient(180deg,var(--blue),var(--blue-deep));border:3px solid #fff;border-radius:10px;padding:10px 14px 0 13px}
.equip-box__title{color:var(--yellow);font-weight:700;font-size:11px;margin-bottom:3px}
.equip-box .checks{font-size:8.4px;line-height:17px}
</style>
</head>
<body>

<!-- FRONT -->
<section class="sheet sheet--front">
  <div class="brand"><span class="brand__dot"></span><span class="brand__name">Tallowmere Gear Hub</span></div>
  <div class="tagline">
    <div class="tagline__services">Rental • Sales • Service</div>
    <div class="tagline__web">www.tallowmeregearhub.com</div>
  </div>

  <svg class="abs" style="left:0;top:0" width="498" height="300" viewBox="0 0 498 300">
    <defs>
      <linearGradient id="heroFill" x1="0" y1="0" x2="1" y2="1">
        <stop offset="0" stop-color="#f2e2c0"/>
        <stop offset=".45" stop-color="#d7a35b"/>
        <stop offset=".7" stop-color="#8d8d8d"/>
        <stop offset="1" stop-color="#5d5d5d"/>
      </linearGradient>
    </defs>
    <path role="img" aria-label="Service truck and flatbed trailer loaded with cooling units, fans and heaters" d="M0 95 C150 80 350 70 498 85 L498 195 C380 250 200 262 0 258 Z" fill="url(#heroFill)"/>
    <path d="M0 258 C200 262 380 250 498 195 L498 220 C380 280 200 297 0 293 Z" fill="var(--red)"/>
  </svg>
  <div class="hero-badge">KESTREL<br>DUNE<br>EQUIPMENT</div>

  <div class="tab" style="left:0;top:313px;width:180px;height:25px;font-size:19px">KESTREL DUNE</div>
  <ul class="bullets intro">
    <li>Kestrel Dune is the process or technique of arresting the ripening of fruits and vegetables after harvesting by immersion of ice or cold water.</li>
    <li>Fruits and vegetables can be cooled rapidly by bringing them in contact with cold moving water.</li>
  </ul>

  <div class="strengths">
    <ul class="checks">
      <li>24/7 Rapid Response</li>
      <li>Nationwide Service Area</li>
      <li>Unparalelled Customer Service</li>
      <li>Over 25 years of experience in HVAC and power</li>
      <li>Customization of equipment to meet individual customer needs</li>
      <li>Delivery &amp; installation of all equipment</li>
      <li>Extensive fleet inventory</li>
      <li>Trailers up to 48' long</li>
    </ul>
  </div>

  <div class="photo photo--warm" role="img" aria-label="Boxed produce stacked in a cooler room" style="left:23px;top:434px;width:114px;height:74px"></div>
  <div class="photo photo--warm" role="img" aria-label="Hose connected at a trailer loading dock" style="left:145px;top:434px;width:114px;height:74px"></div>
  <div class="photo photo--warm" role="img" aria-label="Trailer parked at a cooling dock" style="left:23px;top:514px;width:114px;height:69px"></div>
  <div class="photo photo--warm" role="img" aria-label="Green hoses laid across a warehouse floor" style="left:145px;top:514px;width:114px;height:69px"></div>
  <div class="cutout" role="img" aria-label="Portable yellow floor fan on a wheeled frame" style="left:380px;top:450px;width:100px;height:120px;border-radius:40% 40% 12px 12px;background:radial-gradient(circle at 55% 35%,#f3d62a,#8a7a28 60%,rgba(0,0,0,0) 72%)"></div>

  <div class="footer">
    <span class="footer__cta">CALL FOR YOUR QUOTE TODAY</span>
    <span class="footer__phone">
      <svg width="20" height="20" viewBox="0 0 20 20" aria-hidden="true"><circle cx="10" cy="10" r="8.5" fill="none" stroke="var(--yellow)" stroke-width="2"/><path d="M7 5.5l1.6 2.3-1 1.1c.6 1.3 1.6 2.3 2.9 2.9l1.1-1 2.3 1.6-.8 1.6c-3.4-.3-6.4-3.3-6.7-6.7z" fill="var(--yellow)"/></svg>
      888-412-7086
    </span>
  </div>
</section>

<!-- BACK -->
<section class="sheet sheet--back">
  <div class="brand" style="left:20px"><span class="brand__dot"></span><span class="brand__name">Tallowmere Gear Hub</span></div>
  <div class="tagline" style="top:28px;right:31px">
    <div class="tagline__services">Rental • Sales • Service</div>
    <div class="tagline__web">www.tallowmeregearhub.com</div>
  </div>

  <div class="benefits-panel"></div>
  <div class="tab" style="left:239px;top:90px;width:178px;height:26px;font-size:18px;padding-left:12px">PRODUCT BENEFITS</div>
  <ul class="bullets benefits">
    <li>Kestrel Dune does not remove water from the product and can even revive slightly wilted produce.</li>
    <li>Kestrel Dune increases shelf life through temperature control of fresh produce &amp; helps with flavor retention.</li>
    <li>Kestrel Dune helps ensure product quality retention: temperature and humidity control in post harvest help prevent tissue damage and promote shelf life.</li>
    <li>Kestrel Dune controls field temperatures, which prevents extreme product weight loss caused by dehydration.</li>
    <li>Kestrel Dune is one of the fastest pre-cooling methods: when temperature rises, respiration and heat generation also increase, which decreases shelf time.</li>
    <li>Kestrel Dune allows fruit to be showered with water to avoid "channeling" (water pouring through larger openings where there is less resistance</li>
  </ul>

  <div class="photo photo--truck" role="img" aria-label="Trailer backed against a red warehouse wall" style="left:23px;top:90px;width:181px;height:111px"></div>
  <div class="photo photo--produce" role="img" aria-label="Carrots being showered with cold water on a conveyor" style="left:23px;top:217px;width:181px;height:108px"></div>

  <div class="equip-box">
    <div class="equip-box__title">TALLOWMERE GEAR HUB EQUIPMENT BENEFITS</div>
    <ul class="checks">
      <li>Kestrel Dune equipment is 15x faster than air, allowing for increased production and labor savings.</li>
      <li>Kestrel Dune equipment is 30% more efficient than air, resulting in power consumption savings.</li>
      <li>Kestrel Dune equipment- our systems are more flexible and can be designed and installed on large and small scales.</li>
      <li>Kestrel Dune equipment: Can be used with various packaging options.</li>
    </ul>
  </div>
  <div class="cutout" role="img" aria-label="Large silver portable heater on a blue wheeled frame" style="left:301px;top:441px;width:183px;height:122px;border-radius:40%;background:radial-gradient(ellipse at 50% 45%,#eeeeee,#a9b0b8 55%,rgba(0,0,0,0) 72%)"></div>

  <div class="photo photo--trailer" role="img" aria-label="Yellow cooling unit mounted on an open trailer" style="left:23px;top:474px;width:181px;height:101px"></div>

  <div class="footer">
    <span class="footer__cta">CALL FOR YOUR QUOTE TODAY</span>
    <span class="footer__phone">
      <svg width="20" height="20" viewBox="0 0 20 20" aria-hidden="true"><circle cx="10" cy="10" r="8.5" fill="none" stroke="var(--yellow)" stroke-width="2"/><path d="M7 5.5l1.6 2.3-1 1.1c.6 1.3 1.6 2.3 2.9 2.9l1.1-1 2.3 1.6-.8 1.6c-3.4-.3-6.4-3.3-6.7-6.7z" fill="var(--yellow)"/></svg>
      888-412-7086
    </span>
  </div>
</section>

</body>
</html>
```